I have a business that exists already (Wrenfield Academy of Music) that we offer music lessons to all instruments. I recently opened a smaller version called CHORDS by Wrenfield that will only teach piano lessons. What I'm looking for now is a 3 page Website on word press. After I choose the design I like I want to be able to take over the website and bring it to our hosting company. We want full control of it and our team will take over. The reason I'm doing this is to have other visions and ideas from others. The first page will be about the company and our message/vision. Second page about the piano lessons. The third will be about franchising this concept "Chords by Wrenfield" Attached are 3 Logos . Please refer to our existing website www.wrenfieldmusicacademy.example to look at our piano page and franchising page. Please feel free to message me if you need more info. Thanks
Please note I do not want the new website (Chords by Wrenfield) To look like the other Website (Wrenfield Academy of Music) Fresh new look. I do not want the colours red or using the Red logo. I only provided it so that you have an Idea of What the other business looks like and that you can take the piano content and franchise content off of it. Chords by Wrenfield is smaller concept and only piano lessons.
Thanks
Target Market(s)
Only Piano lessons for all students
Number of Pages Required
3 page
Look and feel

```html
<!DOCTYPE html>
<html lang="en">
<head>
<meta charset="utf-8">
<title>Chords by Wrenfield — Piano Courses</title>
<link rel="stylesheet" href="https://fonts.googleapis.com/css2?family=Montserrat:wght@400;500;600;700&family=Oswald:wght@300;400&family=Ubuntu:wght@300;400;500&display=swap">
<style>
:root{
  --purple:#2d0d5b;
  --purple-deep:#230a49;
  --purple-card:rgba(45,14,92,.88);
  --pink:#d3237c;
  --pink-dark:#b81a6a;
  --ink:#333;
  --muted:#666;
  --line:#e4e4e4;
  --paper:#f6f6f6;
  --white:#fff;
}
*{margin:0;padding:0;box-sizing:border-box}
html,body{width:1200px;height:5168px;overflow:hidden}
body{font-family:"Montserrat",sans-serif;color:var(--ink);background:var(--white);position:relative}
section,header,footer{position:relative;width:1200px;overflow:hidden}
.abs{position:absolute}
.eyebrow{font-family:"Montserrat",sans-serif;font-size:13px;letter-spacing:5px;text-transform:uppercase;font-weight:500}
.title{font-family:"Ubuntu",sans-serif;font-weight:400;font-size:23px;line-height:35px}
.body{font-size:10.5px;line-height:21px;color:var(--muted)}
.rule{width:130px;height:2px;background:currentColor;opacity:.5}
.btn{display:inline-flex;height:38px;border-radius:5px;overflow:hidden;font-size:10px;font-weight:700;text-transform:uppercase;color:var(--white);letter-spacing:.2px}
.btn b{background:var(--pink);display:flex;align-items:center;padding:0 16px;font-weight:700}
.btn i{background:var(--purple);display:flex;align-items:center;justify-content:center;width:46px;gap:3px}
.btn i s{display:block;width:4px;height:4px;border-radius:50%;background:var(--white)}
.btn i s:nth-child(2){width:6px;height:6px}
.ph{position:absolute}

/* header */
.site-header{height:185px;background:var(--purple)}
.topbar{height:36px;border-bottom:1px solid rgba(255,255,255,.12);font-size:9px;color:var(--white);font-weight:600}
.follow{left:198px;top:12px;display:flex;align-items:center;gap:6px}
.sq{display:inline-block;width:14px;height:14px;border:1.5px solid currentColor;border-radius:2px}
.toplinks{right:198px;top:12px;display:flex;gap:24px}
.toplinks span::before{content:"";display:inline-block;width:7px;height:7px;border-radius:50%;background:var(--white);margin-right:6px;vertical-align:-1px}
.brand{left:0;width:1200px;top:66px;text-align:center;font-family:"Ubuntu",sans-serif;color:var(--white);font-size:30px;letter-spacing:1px}
.brand small{font-size:14px;letter-spacing:.5px;margin-left:4px}
.nav{left:0;width:1200px;top:150px;display:flex;justify-content:center;align-items:center;gap:0;font-size:9.5px;font-weight:600;color:var(--white)}
.nav span{width:108px;text-align:center}
.nav .on{color:var(--pink)}
.nav .enrol{background:var(--pink);border:2px solid #ffffff55;border-radius:4px;padding:7px 10px;width:auto;margin-left:18px}

/* hero */
.hero{height:533px}
.hero .ph{inset:0;background:linear-gradient(100deg,#2b1206 0%,#6a3716 35%,#3a1a0a 60%,#1b0d07 100%)}
.hero h1{left:198px;top:88px;font-family:"Oswald",sans-serif;font-weight:300;color:var(--white);font-size:39px;line-height:48px}
.hero h1 em{display:block;font-style:normal;color:var(--pink);font-weight:400;font-size:36px;margin-top:18px}
.hero p{left:198px;top:212px;width:500px;color:var(--white);font-size:16.5px;line-height:32px}
.hero .btn{left:198px;top:332px}

/* inspired band */
.inspired{height:344px;background:var(--pink);color:var(--white);text-align:center}
.inspired .eyebrow{position:absolute;left:0;top:58px;width:100%;font-size:11px;letter-spacing:5px}
.inspired .title{position:absolute;left:0;top:104px;width:100%;font-size:27px;line-height:42px;font-weight:300}
.inspired svg{position:absolute;left:0;bottom:0}

/* about */
.about{height:408px}
.about .eyebrow{left:200px;top:50px;color:var(--ink)}
.about .title{left:200px;top:76px}
.about .body{left:200px;top:152px;width:430px}
.about .btn{left:202px;top:296px}
.about .ph{left:690px;top:55px;width:310px;height:281px;background:linear-gradient(135deg,#caa690,#3a2a26 60%,#f3f3f3)}

/* courses */
.courses{height:825px}
.courses .ph{inset:0;background:linear-gradient(90deg,#140a10 0%,#2d1a18 45%,#6a3e2c 75%,#2a130c 100%)}
.courses .eyebrow{left:0;top:80px;width:100%;text-align:center;color:var(--white);font-size:12px}
.courses .title{left:0;top:110px;width:100%;text-align:center;color:var(--white)}
.courses .rule{left:535px;top:168px;color:var(--white)}
.card{position:absolute;width:249px;height:185px;background:var(--purple-card);color:var(--white);text-align:center;display:flex;flex-direction:column;justify-content:center;padding:0 18px}
.card h3{font-family:"Ubuntu",sans-serif;font-weight:400;font-size:17px;margin-bottom:14px}
.card p{font-size:9.5px;line-height:21px;font-weight:500}
.card.on{background:var(--pink)}
.courses .btn{left:506px;top:697px}

/* exceptional */
.exceptional{height:598px}
.exceptional .eyebrow{left:200px;top:94px}
.exceptional .title{left:200px;top:122px;width:420px}
.points{left:195px;top:248px;width:456px}
.points li{list-style:none;height:40px;background:var(--paper);margin-bottom:8px;display:flex;align-items:center;padding-left:14px;font-size:10px;font-weight:600;text-transform:uppercase}
.points li::before{content:"+";color:var(--pink);font-size:17px;font-weight:600;margin-right:10px}
.exceptional .btn{left:198px;top:472px}
.exceptional .ph{left:690px;top:98px;width:310px;height:407px;background:linear-gradient(150deg,#d7b9a6,#4a1b1c 45%,#20090b 100%)}

/* franchise */
.franchise{height:485px;background:radial-gradient(ellipse at 40% 55%,#5b1fa0 0%,var(--purple) 55%,var(--purple-deep) 100%);color:var(--white)}
.franchise .ph{left:215px;top:140px;width:290px;height:220px;background:radial-gradient(ellipse at 50% 70%,#3f156f,#2a0a55 70%,transparent 72%)}
.franchise .eyebrow{left:690px;top:84px;font-size:12px}
.franchise .title{left:690px;top:110px;width:320px}
.franchise .rule{left:690px;top:188px}
.franchise .text{left:690px;top:222px;width:310px;font-size:10.5px;line-height:21px;font-weight:500}
.franchise .btn{left:690px;top:340px}
.franchise .btn i{background:transparent;border:1px solid #ffffff66;border-left:0;border-radius:0 5px 5px 0}

/* testimonial */
.testimonial{height:614px;color:var(--white);text-align:center}
.testimonial .ph.bg{inset:0;background:linear-gradient(90deg,#1f0e07 0%,#4a2611 40%,#24110a 70%,#120806 100%)}
.avatar{left:540px;top:76px;width:118px;height:118px;border-radius:50%;border:4px solid var(--white);background:linear-gradient(135deg,#b8b2ad,#e7e2de)}
.testimonial blockquote{position:absolute;left:340px;width:520px;top:238px;font-style:italic;font-size:14.5px;line-height:31px}
.testimonial cite{position:absolute;display:block;left:0;width:1200px;top:362px;text-align:center;font-style:normal;font-size:13px}
.testimonial cite b{font-weight:700}
.dots{left:563px;top:448px;display:flex;gap:6px}
.dots s{width:10px;height:10px;border-radius:50%;border:1.5px solid var(--white)}
.dots s:first-child{background:var(--white)}
.testimonial .btn{left:512px;top:518px}

/* blog */
.blog{height:798px;background:var(--paper)}
.blog .eyebrow{left:0;top:98px;width:100%;text-align:center;font-size:12px}
.blog .title{left:0;top:124px;width:100%;text-align:center}
.blog .rule{left:535px;top:182px;color:var(--pink)}
.post{position:absolute;top:219px;width:249px;height:365px;background:var(--white)}
.post .ph{left:0;top:0;width:249px;height:166px}
.post h4{position:absolute;left:15px;top:186px;width:225px;font-family:"Ubuntu",sans-serif;font-weight:400;font-size:13.5px;line-height:25px}
.post .meta{position:absolute;left:18px;top:242px;width:225px;font-size:9px;line-height:18px;color:var(--muted)}
.post .meta a{color:var(--pink);text-decoration:none}
.post .more{position:absolute;left:18px;top:306px;font-size:9.5px;color:var(--ink)}
.post .cm{position:absolute;right:26px;top:306px;font-size:9.5px;color:var(--pink)}
.pager{right:200px;top:651px;display:flex;gap:6px}
.pager span{width:22px;height:22px;border:1px solid var(--line);background:var(--white);font-size:8px;display:flex;align-items:center;justify-content:center;color:var(--muted)}
.pager .on{background:var(--pink);color:var(--white);border-color:var(--pink)}
.blog .btn{left:528px;top:712px}

/* footer */
.site-footer{height:285px;background:var(--white);font-size:9.5px;color:var(--muted);line-height:20px}
.site-footer h5{font-size:9.5px;font-weight:700;color:var(--ink);margin-bottom:20px;text-transform:uppercase}
.col{top:70px}
.contact li{list-style:none;display:flex;gap:10px;margin-bottom:10px;line-height:20px}
.contact svg{flex:none;margin-top:5px}
.contact b{color:var(--ink);font-weight:600}
.bottombar{height:93px;border-top:1px solid var(--line);font-size:9.5px;color:var(--muted)}
.bottombar .copy{left:198px;top:24px}
.bottombar .soc{right:198px;top:20px;display:flex;gap:5px;color:var(--purple)}
</style>
</head>
<body>

<header class="site-header">
  <div class="topbar">
    <div class="abs follow">Follow Us: <span class="sq"></span><span class="sq"></span><span class="sq"></span><span class="sq"></span><span class="sq"></span></div>
    <div class="abs toplinks"><span>FAQ</span><span>Blog</span></div>
  </div>
  <div class="abs brand">CHORDS<small>by Wrenfield</small></div>
  <nav class="abs nav">
    <span class="on">HOME</span><span>ABOUT US</span><span>PIANO COURSES</span><span>FRANCHISE</span><span>CONTACT</span><span class="enrol">ENROL TODAY!</span>
  </nav>
</header>

<section class="hero">
  <div class="ph" role="img" aria-label="Woman playing an upright piano by candlelight"></div>
  <h1 class="abs">CANADA'S QUINTESSENTIAL<em>PIANO COURSES FOR KIDS &amp; ADULTS</em></h1>
  <p class="abs">Lorem Ipsum is simply dummy text of the printing and typesetting industry. Lorem Ipsum has been the ...</p>
  <a class="abs btn"><b>Piano Courses</b><i><s></s><s></s><s></s></i></a>
</section>

<section class="inspired">
  <div class="eyebrow">Inspired by passion and excellence</div>
  <h2 class="title">The most comprehensive piano<br>instruction in Canada</h2>
  <svg width="1200" height="100" viewBox="0 0 1200 100" aria-hidden="true"><polygon points="0,100 0,98 600,0 1200,98 1200,100" fill="#fff"/></svg>
</section>

<section class="about">
  <div class="abs eyebrow">About Us</div>
  <h2 class="abs title">Why Choose Chords by Wrenfield?</h2>
  <p class="abs body">It is a long established fact that a reader will be distracted by the readable content of a page when looking at its layout. The point of using Lorem Ipsum is that it has a more-or-less normal distribution of letters, as opposed to using 'Content here, content here', making it look like readable English. Many desktop publishing packages and web page...</p>
  <a class="abs btn"><b>Read More</b><i><s></s><s></s><s></s></i></a>
  <div class="ph" role="img" aria-label="Two hands playing piano keys"></div>
</section>

<section class="courses">
  <div class="ph" role="img" aria-label="Woman with a shoulder tattoo playing piano in low light"></div>
  <div class="abs eyebrow">Piano Courses</div>
  <h2 class="abs title">Our courses are tailored to suit you!</h2>
  <div class="abs rule"></div>
  <div class="card on" style="left:198px;top:225px"><h3>One Two One</h3><p>Our excellent one to one piano courses are suitable for all adults, from absolute beginners without any prior musical knowledge to advanced amateur pianists.</p></div>
  <div class="card" style="left:475px;top:225px"><h3>CLASSICAL</h3><p>Beginner, Intermediate, Advanced</p></div>
  <div class="card" style="left:752px;top:225px"><h3>JAZZ</h3><p>Beginner, Intermediate, Advanced</p></div>
  <div class="card" style="left:198px;top:446px"><h3>POP</h3><p>Beginner, Intermediate, Advanced</p></div>
  <div class="card" style="left:475px;top:446px"><h3>Rock</h3><p>Beginner, Intermediate, Advanced</p></div>
  <div class="card" style="left:752px;top:446px"><h3>BLUES</h3><p>Beginner, Intermediate, Advanced</p></div>
  <a class="abs btn"><b>View Our Piano Courses</b><i><s></s><s></s><s></s></i></a>
</section>

<section class="exceptional">
  <div class="abs eyebrow">Exceptional Piano Instruction</div>
  <h2 class="abs title">We are devoted to providing adults and kids with the most exceptional piano</h2>
  <ul class="abs points">
    <li>We provide you with a platform</li>
    <li>You don't need any special talent</li>
    <li>We are committed to your learning</li>
    <li>Core beliefs to make you a success!</li>
  </ul>
  <a class="abs btn"><b>10 More Reason to Enroll</b><i><s></s><s></s><s></s></i></a>
  <div class="ph" role="img" aria-label="Hands with a bracelet playing a piano keyboard"></div>
</section>

<section class="franchise">
  <div class="ph" role="img" aria-label="Grand piano standing on a curved keyboard"></div>
  <div class="abs eyebrow">Franchise</div>
  <h2 class="abs title">Piano lessons are the ultimate franchise</h2>
  <div class="abs rule"></div>
  <p class="abs text">The largest music school franchise in Canada<br>We believe that every child should be given the opportunity to be exposed to music, enriching their lives inside and outside the classroom.</p>
  <a class="abs btn"><b>Find Out More</b><i><s></s><s></s><s></s></i></a>
</section>

<section class="testimonial">
  <div class="ph bg" role="img" aria-label="Hands playing an old upright piano"></div>
  <div class="ph avatar" role="img" aria-label="Student portrait"></div>
  <blockquote>Lorem Ipsum is simply dummy text of the printing and typesetting industry. Lorem Ipsum has been the industry's standard dummy text ever since .</blockquote>
  <cite><b>Dana Whitlock</b>, Student, One to One</cite>
  <div class="abs dots"><s></s><s></s><s></s><s></s></div>
  <a class="abs btn"><b>Visit Our Testimonials</b><i><s></s><s></s><s></s></i></a>
</section>

<section class="blog">
  <div class="abs eyebrow">Blog</div>
  <h2 class="abs title">Our latest news, tips and tricks</h2>
  <div class="abs rule"></div>
  <article class="post" style="left:198px">
    <div class="ph" role="img" aria-label="Hands on piano keys" style="background:linear-gradient(135deg,#f2f2f2,#9a8c86 60%,#5d4a6a)"></div>
    <h4>The basics of jazz for the adult beginner</h4>
    <p class="meta">By <a>Wrenfield Academy</a> | April 30th, 2020 |<br>Tags: <a>Jazz piano, learning jazz piano</a></p>
    <span class="more">Read More ›</span><span class="cm">○ 0</span>
  </article>
  <article class="post" style="left:475px">
    <div class="ph" role="img" aria-label="Woman playing piano in a dark room" style="background:linear-gradient(135deg,#2a1a16,#6b4a3c 55%,#1a0f0c)"></div>
    <h4>The basics of jazz for the adult beginner</h4>
    <p class="meta">By <a>Wrenfield Academy</a> | April 30th, 2020 |<br>Tags: <a>Jazz piano, learning jazz piano</a></p>
    <span class="more">Read More ›</span><span class="cm">○ 0</span>
  </article>
  <article class="post" style="left:752px">
    <div class="ph" role="img" aria-label="Woman at an upright piano with warm light" style="background:linear-gradient(135deg,#3a1a0c,#8a4a22 50%,#24100a)"></div>
    <h4>Five benefits of learning the piano in small group format</h4>
    <p class="meta">By <a>Wrenfield Academy</a> | April 28th, 2020 |<br>Tags: <a>Jazz piano, learning jazz piano</a></p>
    <span class="more">Read More ›</span><span class="cm">○ 0</span>
  </article>
  <div class="abs pager"><span class="on">1</span><span>2</span><span>›</span></div>
  <a class="abs btn"><b>Visit Our Blog</b><i><s></s><s></s><s></s></i></a>
</section>

<footer class="site-footer">
  <div class="abs col" style="left:198px;width:200px">
    <h5>Chords by Wrenfield</h5>
    <ul class="contact">
      <li><svg width="10" height="10" viewBox="0 0 10 10"><path d="M2 0l2 2.5-1 1.2c.6 1.3 1.6 2.3 2.9 2.9L7 5.6 10 7.5 9 10C4 10 0 6 0 1z" fill="#666"/></svg><span><b>Inquiries:</b> 1-800-555-0142 <br><b>Franchising:</b> 905-555-0187</span></li>
      <li><svg width="10" height="8" viewBox="0 0 10 8"><rect x=".5" y=".5" width="9" height="7" fill="none" stroke="#666"/><path d="M.5.5L5 4.5 9.5.5" fill="none" stroke="#666"/></svg><span>info@chordsbywrenfield.example</span></li>
      <li><svg width="10" height="10" viewBox="0 0 10 10"><circle cx="5" cy="5" r="4.5" fill="none" stroke="#666"/><path d="M5 2.5V5h2" fill="none" stroke="#666"/></svg><span>Mon to Sat: Visit strictly<br>by appointment</span></li>
    </ul>
  </div>
  <div class="abs col" style="left:433px"><h5>Lessons &amp; Enrolment</h5>Piano Lessons<br>FAQ<br>Enrol Now<br>Student Concerts<br>Corporate</div>
  <div class="abs col" style="left:654px"><h5>Courses</h5>Classical<br>Jazz<br>Blues<br>Popular<br>Rock<br>One-to-One<br>Group</div>
  <div class="abs col" style="left:835px"><h5>Resources</h5>Piano Resources<br>Blog Posts<br>Piano Shops<br>Piano Tuners &amp; Technicians</div>
</footer>

<section class="bottombar">
  <div class="abs copy">© Chords by Wrenfield &nbsp;|&nbsp; All Rights Reserved &nbsp;|&nbsp; enrol@chordsbywrenfield.example</div>
  <div class="abs soc"><span class="sq"></span><span class="sq"></span><span class="sq"></span><span class="sq"></span><span class="sq"></span></div>
</section>

</body>
</html>
```